Product Designer Business Card

Small product design, engineering and prototyping firm in need of a clean, professional business card design. To support our 3D design and drawing services, we offer 3D printing, molding, and casting of plastics, silicones, resins, etc. Our logo can still be modified/changed if necessary. The red/orange color is preferred, but may be substituted with blue or green, potentially. Either way, the colour of the logo should be match/compliment colors used throughout the design. One thought is to have the logo/contact info on one side, with the other side describing services offered, like with a small icon of 3D printer, molding, casting, and computer with a 3D model on-screen.
Industry/Entity Type
Mechanical Engineering
Contact Information for Business Card
Company: Halvick Design
Phone: 613-582-4179
Email: myles@halvickdesign.ca

```html
<!DOCTYPE html>
<html lang="en">
<head>
<meta charset="utf-8">
<title>Halvick Design — Business Card</title>
<link rel="stylesheet" href="https://fonts.googleapis.com/css2?family=Montserrat:wght@300;700&display=swap">
<style>
  :root {
    --backdrop: #ecebe8;
    --card: #ffffff;
    --ink: #1f1d1c;
    --accent: #d95a1b;
    --card-shadow: rgba(0, 0, 0, 0.14);
  }
  * { box-sizing: border-box; }
  html, body {
    margin: 0;
    width: 1200px;
    height: 840px;
    overflow: hidden;
    background: var(--backdrop);
    font-family: "Montserrat", Arial, sans-serif;
    color: var(--ink);
  }
  .stage {
    width: 1200px;
    height: 840px;
    display: flex;
    align-items: center;
    justify-content: center;
  }
  .business-card {
    position: relative;
    width: 875px;
    height: 500px;
    background: var(--card);
    box-shadow: 0 14px 40px var(--card-shadow);
    padding: 64px 72px;
  }
  .services {
    margin: 0;
    font-weight: 300;
    font-size: 19px;
    letter-spacing: 0.32em;
    text-transform: uppercase;
  }
  .services .divider { padding: 0 0.35em; }
  .brand {
    position: absolute;
    left: 72px;
    top: 178px;
    display: flex;
    align-items: center;
    gap: 22px;
  }
  .brand-mark {
    width: 46px;
    height: 46px;
    background: var(--accent);
  }
  .brand-name {
    margin: 0;
    font-weight: 700;
    font-size: 58px;
    letter-spacing: 0.12em;
    text-transform: uppercase;
    color: var(--ink);
    line-height: 1;
  }
  .contact {
    position: absolute;
    left: 72px;
    bottom: 64px;
    font-style: normal;
    font-weight: 300;
    text-transform: uppercase;
    letter-spacing: 0.14em;
    line-height: 1.3;
  }
  .contact .phone {
    display: block;
    font-size: 34px;
    padding-left: 140px;
  }
  .contact .email {
    display: block;
    font-size: 34px;
  }
</style>
</head>
<body>
  <main class="stage">
    <article class="business-card">
      <p class="services">3D Printing<span class="divider">|</span>Molding<span class="divider">|</span>Casting</p>
      <div class="brand">
        <span class="brand-mark" aria-hidden="true"></span>
        <h1 class="brand-name">Halvick Design</h1>
      </div>
      <address class="contact">
        <span class="phone">613-582-4179</span>
        <span class="email">myles@halvickdesign.ca</span>
      </address>
    </article>
  </main>
</body>
</html>
```